Brodwin and Partners Outpatient Imaging

1. flyer/rack card size, front and back for imaging services advertisement. Color design. Text file and one chest xray and one hand radiograph hopefully. Clean and easy to read. 2. clear to read title about "Outpatient imaging services" 3. Only using images and text provided. This is a radiology group offering web based image interpretation to physicians in the community.

Target Market(s)

Referring outpatient physicians

Industry/Entity Type

Medical Imaging

Font styles to use
Serif

Requirements
Must have
• preferably one picture, easy to read design
Nice to have
• both a hand and chest xray would be nice.

```html
<!DOCTYPE html>
<html lang="en">
<head>
<meta charset="utf-8">
<title>Brodwin and Partners Outpatient Imaging</title>
<link href="https://fonts.googleapis.com/css2?family=Bebas+Neue&family=Raleway:wght@400&family=Open+Sans:wght@700&display=swap" rel="stylesheet">
<style>
  :root {
    --blue-deep: #173f6e;
    --blue-mid: #2a67a3;
    --blue-light: #3f86c4;
    --white: #ffffff;
    --accent-red: #b3202a;
    --base-dark: #2b2b2d;
  }
  html, body {
    margin: 0;
    padding: 0;
    width: 1200px;
    height: 2557px;
    overflow: hidden;
    background: var(--base-dark);
  }
  .card {
    position: relative;
    width: 1200px;
    height: 2557px;
    overflow: hidden;
    color: var(--white);
  }
  .xray-backdrop {
    position: absolute;
    left: 0; top: 0;
    width: 1200px; height: 2414px;
    background:
      radial-gradient(ellipse 620px 900px at 700px 900px, rgba(150,190,230,0.28), transparent 70%),
      radial-gradient(ellipse 500px 500px at 1100px 80px, rgba(10,30,60,0.55), transparent 70%),
      linear-gradient(180deg, var(--blue-deep) 0%, var(--blue-mid) 35%, var(--blue-mid) 65%, var(--blue-light) 100%);
  }
  .accent-stripe {
    position: absolute;
    left: 0; top: 2414px;
    width: 1200px; height: 20px;
    background: var(--accent-red);
  }
  .base-band {
    position: absolute;
    left: 0; top: 2434px;
    width: 1200px; height: 123px;
    background: var(--base-dark);
  }
  .body-copy {
    position: absolute;
    left: 80px;
    width: 1050px;
    margin: 0;
    font-family: "Raleway", sans-serif;
    font-weight: 400;
    font-size: 36.5px;
    line-height: 44px;
  }
  .intro { top: 12px; }
  .services-copy { top: 700px; }
  .section-title {
    position: absolute;
    left: 80px;
    top: 616px;
    margin: 0;
    font-family: "Bebas Neue", sans-serif;
    font-weight: 400;
    font-size: 78px;
    line-height: 78px;
    letter-spacing: 1px;
  }
  .closing-statement {
    position: absolute;
    left: 60px;
    width: 1080px;
    top: 1336px;
    margin: 0;
    text-align: center;
    font-family: "Bebas Neue", sans-serif;
    font-weight: 400;
    font-size: 84px;
    line-height: 80px;
    letter-spacing: 1.5px;
  }
  .contact-call {
    position: absolute;
    left: 60px;
    width: 1080px;
    top: 1652px;
    margin: 0;
    text-align: center;
    font-family: "Open Sans", sans-serif;
    font-weight: 700;
    font-size: 39px;
    line-height: 54px;
  }
  .practice-name {
    position: absolute;
    left: 190px;
    top: 2070px;
    display: flex;
    align-items: center;
    gap: 40px;
  }
  .practice-name .name-text {
    font-family: "Raleway", sans-serif;
    font-weight: 400;
    font-size: 56px;
    line-height: 64px;
    letter-spacing: 2px;
    color: var(--white);
  }
  .practice-name .mark-dot {
    width: 150px;
    height: 150px;
    border-radius: 50%;
    background: var(--white);
    opacity: 0.9;
    flex: none;
  }
</style>
</head>
<body>
<main class="card">
  <div class="xray-backdrop" role="img" aria-label="Faint chest radiograph in blue tones behind the text"></div>

  <p class="body-copy intro">With our dedication to quality patient care, the doctors and staff of Brodwin and Partners go above and beyond to assure your office needs are met. We will work with you through image interpretation, imaging follow-up, and are committed to your confidence in our process. Our goal is to help you integrate our services to create a superior diagnostic and treatment process that works for you and your practice.</p>

  <h2 class="section-title">OUR OUTPATIENT SERVICES</h2>

  <p class="body-copy services-copy">We identified a need in our communities to provide a better product for our physicians when choosing office based imaging. In 2015 we began working with Lumora Health to provide image interpretation while utilizing state of the art medical data and image management. As a physician owned practice, we pride ourselves on providing high quality and accurate reports with rapid results (a final report within 24 hours). We offer a 24 hour direct phone line for referring physicians to speak with one of our radiologists should a problem arise after hours.</p>

  <h2 class="closing-statement">WE LOOK FORWARD TO BEING A<br>COMPLETE SOLUTION FOR ALL OF<br>YOUR IMAGING NEEDS.</h2>

  <p class="contact-call">To hear more about our outpatient services<br>or free in office set up, please contact<br>Dr. Elena Marsh at 555-014-2290.</p>

  <div class="practice-name">
    <div class="name-text">BRODWIN AND<br>PARTNERS, P.C.</div>
    <div class="mark-dot"></div>
  </div>

  <div class="accent-stripe"></div>
  <div class="base-band"></div>
</main>
</body>
</html>
```